依頼詳細
会社の名刺を新しくしたいと思っております。移転予定がありますので、フォントに関してはイラストレーターCS6に入っているものでアウトラインへ変更なしでお願いします。
記載項目
表面:ロゴ、会社名、会社住所、役職、名前、電話番号、ファックス番号、携帯番号、メール、HP
裏面:事業内容(販売事業、ロジスティック事業、生産事業、エネルギー事業)、店舗ロゴ(風見屋)、営業所
希望イメージ
シンプル 複雑
単色 カラフル
暗い 明るい
日常 高級
遊び心 厳粛
未来的 伝統的
女性的 男性的
希望する色
茶系、黄・オレンジ系
納品ファイル
• イラストレーター形式 (.ai)
補足説明
現在、使用している名刺とロゴを追加します。
名刺裏面の風見屋ロゴを追加致します。

サンプルで提示した名刺裏面の事業内容ですが、細かい内容は省いて頂いて結構です。

宜しくお願い致します。
お世話になっております。

ご要望と致しましては、シンプルでスタイリッシュな名刺を希望しております。
裏面ですが、事業内容は4つの記載だけで添付ファイルのように、細かい記載は省いていただいて結構です。
内容は下記をご参照ください。

上記の記載でお願い致します。

名刺に関しましては横型・縦型どちらでも構いません。

宜しくお願い致します。

シンプルで印象に残りましたので選ばして頂きました。
ありがとうございました。

たくさんのご提案ありがとうございました。

```html
<!DOCTYPE html>
<html lang="ja">
<head>
<meta charset="utf-8">
<title>LUMINA 名刺</title>
<link rel="stylesheet" href="https://fonts.googleapis.com/css2?family=Noto+Sans+JP:wght@400;500;700&display=swap">
<style>
  :root {
    --page: #f1f0ee;
    --card: #ffffff;
    --card-edge: #d9d6d2;
    --brown: #6b4a3a;
    --brown-soft: #a58b7c;
    --orange: #e8a03a;
    --yellow: #f0c23b;
    --ink: #3a2e28;
  }
  * { box-sizing: border-box; margin: 0; padding: 0; }
  html, body { width: 847px; height: 1200px; overflow: hidden; }
  body {
    background: var(--page);
    font-family: "Noto Sans JP", sans-serif;
    color: var(--ink);
    position: relative;
  }
  .card {
    position: absolute;
    left: 28px;
    width: 790px;
    background: var(--card);
    border: 1px solid var(--card-edge);
    box-shadow: 0 2px 6px rgba(0,0,0,0.12);
    overflow: hidden;
  }
  .card--front { top: 42px; height: 545px; }
  .card--back { top: 668px; height: 495px; }

  /* front */
  .front-band { position: absolute; inset: 0; }
  .person { position: absolute; left: 110px; top: 50px; text-align: center; }
  .person__title { font-size: 20px; color: var(--ink); letter-spacing: 1px; padding-left: 60px; line-height: 28px; }
  .person__name { font-size: 40px; font-weight: 500; letter-spacing: 6px; line-height: 52px; }
  .person__roman { font-size: 18px; color: var(--ink); line-height: 24px; }

  .brand {
    position: absolute; left: 325px; top: 240px;
    display: flex; align-items: center; gap: 14px;
  }
  .brand__dot { width: 30px; height: 30px; border-radius: 50%; background: var(--orange); }
  .brand__name {
    font-size: 70px; font-weight: 700; color: var(--brown);
    letter-spacing: 4px; line-height: 1;
  }

  .contact {
    position: absolute; left: 520px; top: 410px;
    list-style: none; font-size: 18px; line-height: 24px; color: var(--ink);
  }
  .contact li { display: flex; align-items: center; gap: 8px; white-space: nowrap; }
  .contact svg { width: 15px; height: 15px; fill: var(--orange); flex: none; }

  /* back */
  .shop-mark {
    position: absolute; left: 0; right: 0; top: 48px;
    display: flex; justify-content: center; align-items: center; gap: 10px;
  }
  .shop-mark__square { width: 20px; height: 20px; background: var(--orange); }
  .shop-mark__name { font-size: 44px; font-weight: 700; color: var(--brown); letter-spacing: 4px; }

  .services {
    position: absolute; left: 70px; top: 170px;
    display: grid; grid-template-columns: 330px 300px; row-gap: 16px;
    list-style: none; font-size: 25px;
  }
  .services li { display: flex; align-items: center; gap: 18px; }
  .services li::before {
    content: ""; width: 22px; height: 22px; border-radius: 50%; background: var(--yellow);
  }
  .rule {
    position: absolute; left: 70px; right: 70px; top: 272px;
    height: 3px; background: var(--brown);
  }
  .offices { position: absolute; left: 70px; top: 292px; font-size: 19px; line-height: 27px; }
  .offices dt { font-weight: 500; display: flex; align-items: center; gap: 4px; }
  .offices dt::before { content: ""; width: 12px; height: 12px; background: var(--brown); }
  .offices dd { padding-left: 16px; }
</style>
</head>
<body>

<section class="card card--front">
  <svg class="front-band" viewBox="0 0 790 545" aria-hidden="true">
    <polygon points="0,100 790,330 790,405 0,175" fill="var(--brown-soft)" opacity="0.18"/>
    <line x1="0" y1="100" x2="790" y2="330" stroke="var(--brown)" stroke-width="3"/>
    <line x1="0" y1="175" x2="790" y2="405" stroke="var(--brown)" stroke-width="3"/>
  </svg>

  <div class="person">
    <p class="person__title">代表取締役</p>
    <p class="person__name">森田 早苗</p>
    <p class="person__roman">Sanae Morita</p>
  </div>

  <div class="brand">
    <span class="brand__dot"></span>
    <span class="brand__name">LUMINA</span>
  </div>

  <ul class="contact">
    <li><svg viewBox="0 0 16 16"><path d="M3 1h3l1 4-2 1a9 9 0 0 0 5 5l1-2 4 1v3a2 2 0 0 1-2 2A13 13 0 0 1 1 3a2 2 0 0 1 2-2z"/></svg>0120-45-6700</li>
    <li><svg viewBox="0 0 16 16"><path d="M4 1h7v4H4zM1 6h14v7h-3v2H4v-2H1zM5 10v4h6v-4z"/></svg>0120-45-6701</li>
    <li><svg viewBox="0 0 16 16"><path d="M4 0h8a1 1 0 0 1 1 1v14a1 1 0 0 1-1 1H4a1 1 0 0 1-1-1V1a1 1 0 0 1 1-1zm1 2v10h6V2z"/></svg>0900012-3456</li>
    <li><svg viewBox="0 0 16 16"><path d="M1 3h14v10H1zm1 1v1l6 4 6-4V4z"/></svg>sanae@lumina-example.jp</li>
    <li><svg viewBox="0 0 16 16"><path d="M8 0a8 8 0 1 0 0 16A8 8 0 0 0 8 0zm0 2a6 6 0 1 1 0 12A6 6 0 0 1 8 2z"/></svg>www.lumina-example.jp</li>
  </ul>
</section>

<section class="card card--back">
  <div class="shop-mark">
    <span class="shop-mark__square"></span>
    <span class="shop-mark__name">風見屋</span>
  </div>

  <ul class="services">
    <li>販売事業</li>
    <li>生産事業</li>
    <li>ロジスティック事業</li>
    <li>エネルギー事業</li>
  </ul>

  <div class="rule"></div>

  <dl class="offices">
    <dt>本社</dt>
    <dd>〒100-0000　架空県緑野市花見町森ノ下12-3</dd>
    <dt>北浜営業所</dt>
    <dd>架空県北浜郡北浜町大字川上4521-8</dd>
    <dd>TEL：0120-98-7654</dd>
  </dl>
</section>

</body>
</html>
```